■ 依頼の目的/概要

私は第45回全国青葉学徒競技祭典選手権(以下、葉徒祭)運営委員会の広報局長を務めております。葉徒祭というのは、東日本と西日本から選抜された医学部学生が参加する体育大会で、開催競技は全12競技となっております。

今回は、その大会のPR用に各大学に配布するポスターのデザイン制作をお願いします。

■ 重視する点/検討基準

ポスターを見るのは主に大学医学部の学生で、一目見て葉徒祭のポスターだと分かるものがいいです。

制作する上で、必ず入れてほしいワードを以下に述べておきます。

・第45回全国青葉学徒競技祭典選手権
http://www.hatosai.kumonet.jp/top.htm(※大会HPです)
・主管:白鷺ヶ丘医療学院・浜風医療学院
・主催:北辰学徒競技協会連合・南星学徒競技協会連合
・開催競技(弓道・硬式テニス・軟式テニス・バトミントン・準硬式野球・サッカー・バスケットボール・柔道・卓球・剣道・バレーボール・ヨットの全12競技)

前年度、前々年度のポスターを添付しておりますので、ご参照下さい。

■ 利用用途

A2サイズのポスターに、片面カラーで印刷します。また、大会HPにも掲載いたします。

■ その他/注意点

データはイラストレーター形式(CS3以下)にて縦長使用でお願いします。
そのまま印刷会社に入稿するので、カラーモードはCMYKにて、塗り足し・アウトライン化もお願いします。

・ご提案を選択後に当選者様に修正を依頼する可能性がございますのでご了承下さい。
・選択させて頂いたデザインの著作権(財産権)等の扱いはMokkaro利用規約に従い、弊運営委員会に譲渡をお願いします。フォントや画像素材などを利用する場合は上記利用用途に使用できることを確認し、第三者の知的財産権等に注意して下さい。

葉徒祭につきましては下記のサイトをご参照下さい。何らかのご参考にしていただけると幸いです。また、第45回の大会HPはまだ制作しておりません。
http://www.hatosai.kumonet.jp/top.htm
http://ja.hyakkamori.jp/wiki/%E8%91%89%E5%BE%92%E7%A5%AD

以上、宜しくお願い致します。

たくさんのデザイン提案、どうもありがとうございます。
私1人だけでなく、実行委員何人かで最も相応しいと思われるものを選ばせて頂きたいと思います。
二週間位内には選びたいと思います。
■ 選んだ理由

医学生の部屋に貼っているイメージとの提案で、それが私たちのイメージにぴったりでした。また、大学に貼っていても目を引きそうなデザインでとても気に入りました。

■ 提案者全員のお礼・コメント

たくさんの提案ありがとうございました。
すばらしいものばかりだったので選ぶのに迷いましたが、委員何人かで話し合い今回はこのデザインを選ばせていただくことにしました。

```html
<!DOCTYPE html>
<html lang="ja">
<head>
<meta charset="utf-8">
<title>第45回 全国青葉学徒競技祭典選手権</title>
<link href="https://fonts.googleapis.com/css2?family=Noto+Sans+JP:wght@500;700;900&display=swap" rel="stylesheet">
<style>
  :root {
    --navy-deep: #06123d;
    --navy: #0d2a7a;
    --sky: #5cb8f0;
    --sky-light: #9fdcff;
    --gold-light: #fff3b0;
    --gold: #e2b43c;
    --gold-dark: #8a5a12;
    --ink: #1a2038;
    --white: #ffffff;
    --tile-border: #9aa3ad;
    --figure: #c9ced6;
    --url-red: #ff2a2a;
    --band: #05081c;
  }
  * { margin: 0; padding: 0; box-sizing: border-box; }
  html, body { width: 855px; height: 1200px; overflow: hidden; }
  body { font-family: "Noto Sans JP", sans-serif; background: var(--navy-deep); }

  .poster {
    position: relative;
    width: 855px;
    height: 1200px;
    overflow: hidden;
    background:
      radial-gradient(ellipse 520px 520px at 50% 46%, var(--sky-light) 0%, var(--sky) 28%, var(--navy) 70%, var(--navy-deep) 100%);
  }

  .event-name {
    position: absolute;
    top: 22px; left: 0; width: 100%;
    text-align: center;
    color: var(--white);
    font-weight: 900;
    font-size: 50px;
    letter-spacing: 0.04em;
    line-height: 1;
  }

  .event-title {
    position: absolute;
    top: 88px; left: 0; width: 100%;
    text-align: center;
    font-weight: 900;
    font-size: 118px;
    letter-spacing: 0.22em;
    padding-left: 0.22em;
    line-height: 1;
    background: linear-gradient(180deg, var(--gold-light) 0%, var(--gold) 45%, var(--gold-dark) 55%, var(--gold) 100%);
    -webkit-background-clip: text;
    background-clip: text;
    color: transparent;
    -webkit-text-stroke: 3px var(--navy-deep);
  }

  .emblem {
    position: absolute;
    top: 220px; left: 95px;
    width: 665px; height: 500px;
    border-radius: 50%;
    background: radial-gradient(ellipse at 50% 50%, var(--gold-light) 0%, var(--gold) 35%, rgba(226,180,60,0.35) 62%, rgba(226,180,60,0) 72%);
  }

  .edition {
    position: absolute;
    top: 400px; left: 0; width: 100%;
    text-align: center;
    color: var(--ink);
    font-weight: 900;
    line-height: 1;
  }
  .edition-year { display: block; font-size: 34px; }
  .edition-number { display: block; font-size: 58px; margin-top: 14px; }

  .sports {
    position: absolute;
    top: 790px; left: 80px;
    width: 695px;
    display: grid;
    grid-template-columns: repeat(6, 1fr);
    grid-auto-rows: 135px;
    gap: 10px 8px;
    list-style: none;
  }
  .sport {
    position: relative;
    background: var(--white);
    border: 2px solid var(--tile-border);
    padding: 4px 5px;
  }
  .sport-name {
    font-size: 13px;
    font-weight: 700;
    color: var(--ink);
    line-height: 1.1;
    white-space: nowrap;
  }
  .sport-figure {
    position: absolute;
    left: 18px; right: 18px; top: 26px; bottom: 8px;
    border-radius: 6px;
    background: linear-gradient(180deg, var(--figure), #e6e9ee);
  }

  .organizers {
    position: absolute;
    top: 1088px; left: 80px;
    color: var(--white);
    font-weight: 700;
    font-size: 23px;
    line-height: 1.38;
  }

  .site-band {
    position: absolute;
    bottom: 0; left: 0;
    width: 100%; height: 42px;
    background: var(--band);
    text-align: center;
    color: var(--url-red);
    font-weight: 700;
    font-size: 26px;
    line-height: 42px;
  }
</style>
</head>
<body>
<main class="poster">
  <p class="event-name">全国青葉学徒競技祭典</p>
  <h1 class="event-title">選手権</h1>

  <div class="emblem" role="img" aria-label="金色の王冠と翼を持つ盾のエンブレムと金色の弧"></div>
  <p class="edition">
    <span class="edition-year">2011</span>
    <span class="edition-number">第45回</span>
  </p>

  <ul class="sports">
    <li class="sport"><span class="sport-name">弓道</span><div class="sport-figure" role="img" aria-label="弓道の選手のシルエット"></div></li>
    <li class="sport"><span class="sport-name">硬式テニス</span><div class="sport-figure" role="img" aria-label="硬式テニスの選手のシルエット"></div></li>
    <li class="sport"><span class="sport-name">軟式テニス</span><div class="sport-figure" role="img" aria-label="軟式テニスの選手のシルエット"></div></li>
    <li class="sport"><span class="sport-name">バドミントン</span><div class="sport-figure" role="img" aria-label="バドミントンの選手のシルエット"></div></li>
    <li class="sport"><span class="sport-name">卓球</span><div class="sport-figure" role="img" aria-label="卓球の選手のシルエット"></div></li>
    <li class="sport"><span class="sport-name">バレーボール</span><div class="sport-figure" role="img" aria-label="バレーボールの選手のシルエット"></div></li>
    <li class="sport"><span class="sport-name">準硬式野球</span><div class="sport-figure" role="img" aria-label="野球の選手のシルエット"></div></li>
    <li class="sport"><span class="sport-name">サッカー</span><div class="sport-figure" role="img" aria-label="サッカーの選手のシルエット"></div></li>
    <li class="sport"><span class="sport-name">バスケットボール</span><div class="sport-figure" role="img" aria-label="バスケットボールの選手のシルエット"></div></li>
    <li class="sport"><span class="sport-name">柔道</span><div class="sport-figure" role="img" aria-label="柔道の選手のシルエット"></div></li>
    <li class="sport"><span class="sport-name">剣道</span><div class="sport-figure" role="img" aria-label="剣道の選手のシルエット"></div></li>
    <li class="sport"><span class="sport-name">ヨット</span><div class="sport-figure" role="img" aria-label="ヨットのシルエット"></div></li>
  </ul>

  <div class="organizers">
    <p>主管：白鷺ヶ丘医療学院・浜風医療学院</p>
    <p>主催：北辰学徒競技協会連合・南星学徒競技協会連合</p>
  </div>

  <p class="site-band">http://www.hatosai.kumonet.jp</p>
</main>
</body>
</html>
```